LABEL DESIGNS FOR SKINCARE LINE

Hello we are needing 12 label various label designs but would like to see you design ONE. We will pick winner from this and send the rest.
LABEL SIZE -2x7
JAR SIZE IS - 8oz
LOGOS FILES BELOW
https://files.pavorna-share.net/drive/folders/7xk3q-wumTrazPLoqVnnRTZBKHAE2DpLW
INFORMATION FOR LABEL
Calm Dune Hush Whipped Body Sugar Scrub 8oz
Ideal for all Skin Types
Ingredients:
Pure Cane Sugar, Extra Virgin Coconut Oil, Mango Butter, Kukum Butter, Emulsifying Wax, Jojoba Seed Oil, Sweet Almond Oil, Strawberry Essential Oil, and Pomegranate Essential Oil.
Directions to use Body Sugar Scrub:
Apply to wet skin gently in a circular motion on desired body area, hands, feet, legs, arms, etc. Once you have a good scrub, rinse, pat dry, and enjoy soft, hydrated skin. Best to use in the shower. Use between 2-3 times a week if needed.
*Cautions:
(1) Allergy: Approach this product with extreme caution, if you have allergies
(2) Avoid direct contact with eyes
Storage/Shelf Life of Product:
For best results, stir/mix scrub with the wooden or plastic spoon before each use. The shelf life of all sugar scrubs is 6-8 weeks. Keep the product in a cool, dry place, away from hot or heated temperatures.
All Natural, Cruelty-Free, Vegan Free
No Mineral Oil
No Petroleum
No Parabens

```html
<!DOCTYPE html>
<html lang="en">
<head>
<meta charset="utf-8">
<title>Amber Lark &amp; Co — Whipped Body Sugar Scrub Label</title>
<link rel="stylesheet" href="https://fonts.googleapis.com/css2?family=Roboto+Slab:wght@700&display=swap">
<style>
  :root {
    --page-bg: #d2d2d2;
    --label-white: #ffffff;
    --band-peach: #f3d6c3;
    --band-peach-deep: #eccab4;
    --brand-orange: #e4572e;
    --ink-dark: #2b2b2b;
  }
  * { margin: 0; padding: 0; box-sizing: border-box; }
  html, body {
    width: 1200px;
    height: 900px;
    overflow: hidden;
    background: var(--page-bg);
    font-family: "Roboto Slab", Georgia, serif;
  }
  .canvas {
    position: relative;
    width: 1200px;
    height: 900px;
    display: flex;
    align-items: center;
    justify-content: center;
  }
  .jar-label {
    position: relative;
    width: 1050px;
    height: 300px;
    background: var(--label-white);
    overflow: hidden;
    box-shadow: 0 6px 18px rgba(0, 0, 0, 0.12);
  }
  .label-band {
    position: absolute;
    inset: 0;
    width: 100%;
    height: 100%;
  }
  .brand-name {
    position: absolute;
    top: 34px;
    left: 0;
    width: 100%;
    text-align: center;
    font-weight: 700;
    font-size: 58px;
    line-height: 1;
    color: var(--brand-orange);
    letter-spacing: 0.5px;
  }
  .brand-rule {
    position: absolute;
    top: 0;
    left: 0;
    width: 100%;
    height: 100%;
  }
  .product-info {
    position: absolute;
    top: 196px;
    left: 0;
    width: 100%;
    text-align: center;
    color: var(--ink-dark);
    font-weight: 700;
  }
  .product-title {
    font-size: 26px;
    line-height: 1.25;
  }
  .product-note {
    font-size: 22px;
    line-height: 1.3;
  }
</style>
</head>
<body>
  <main class="canvas">
    <section class="jar-label">
      <svg class="label-band" viewBox="0 0 1050 300" preserveAspectRatio="none" role="img" aria-label="Peach band with a soft star sparkle pattern">
        <path d="M0 150 Q 525 215 1050 170 L1050 300 L0 300 Z" fill="var(--band-peach)"/>
      </svg>
      <h1 class="brand-name">Amber Lark &amp; Co</h1>
      <svg class="brand-rule" viewBox="0 0 1050 300" aria-hidden="true">
        <path d="M300 122 Q 525 146 750 122" fill="none" stroke="var(--brand-orange)" stroke-width="3" stroke-linecap="round"/>
      </svg>
      <div class="product-info">
        <p class="product-title">Calm Dune Hush Whipped Body Sugar Scrub 8oz</p>
        <p class="product-note">Ideal for all Skin Types</p>
      </div>
    </section>
  </main>
</body>
</html>
```